Stationary Design for Quince consultant and support company

We need new stationary designed for a London based support company that provide on-site and remote support services for Quince products. Our clients are both consumers and businesses.

We would like a letterhead, compliment slip, business card and possibly an e-mail signature designed.

Business card designs can be either 1 side or 2, depending on designs we receive we may choose a preference for 1 or 2 sides later on in the design stage.

Designs needs to be at least 300dpi and should be done using CMYK colours.

We want the design to be bold, easy to read, clean and professional.

We have attached our company logo in 2 colour variations (if you need any other source files then please ask).

Our logo colours are as follows:

Blue (85, 50, 0, 0) and Green (50, 0, 100, 0)

We use two different suppliers for out stationary so here are the size dimensions for both. Unfortunately they are ever so slightly different size wise so hopefully we can get something that accommodates both, we can provide dimensions if required for final versions.

Some fonts that have been used before with our company are Probert (for tagline on our company logo) and previously had Nauman used, however we are very much open to seeing what the designers come up with and the fonts mentioned are not a requirement.
Updates

Company details for designs (however the template should be editable for multiple staff) Vorbin Ltd. Registered Office: 62-74 Harlow Lane London N7 2QD 020 7915 3381 www.vorbin.example info@vorbin.example Company is Registered in England and Wales Company No. 07351649 Directors details (if you want to make the template using his details), rest of the details are as above Dan Moss Director dan@vorbin.example

Hi all, Thank you for your submissions so far. Could we please ask that you don't use the logo with the tagline from our website for the stationary designs and only the logos provided in the design brief. For the business cards we are looking at normal rectangular business cards to be used and we can provide a template guide for size if needed, please just ask. Regards Vorbin Team

Target Market(s)

Our target market are consumers (of all ages) and small/medium businesses.

Industry/Entity Type

Business

Font styles to use
Serif
Sans Serif

Requirements
Must have
• At least business card, letterhead and compliment slip submitted (we need all 3 designed this time round)
Should not have
• Business cards should not have the writing "registered office" (letterheads and compliment slips can along the bottom edge)

```html
<!DOCTYPE html>
<html lang="en">
<head>
<meta charset="utf-8">
<title>Vorbin Ltd. – Compliment Slip</title>
<link rel="stylesheet" href="https://fonts.googleapis.com/css2?family=Open+Sans:wght@400;600&family=Saira:wght@700&display=swap">
<style>
  :root {
    --brand-blue: #1d5aa8;
    --brand-green: #8dc63f;
    --tint-blue: #eef3fa;
    --tint-green: #f2f8ea;
    --ink: #231f20;
    --text-grey: #3a3a3a;
    --paper: #ffffff;
    --backdrop: #dcdcdc;
  }
  html, body {
    margin: 0;
    padding: 0;
    width: 1200px;
    height: 1000px;
    overflow: hidden;
    background: var(--backdrop);
  }
  .compliment-slip {
    position: absolute;
    left: 40px;
    top: 250px;
    width: 1120px;
    height: 501px;
    background: var(--paper);
    overflow: hidden;
    font-family: "Open Sans", Arial, sans-serif;
  }
  .decor-area {
    position: absolute;
    left: 566px;
    top: 0;
    right: 0;
    bottom: 0;
    background: linear-gradient(100deg, var(--paper) 0%, var(--tint-blue) 45%, var(--tint-green) 100%);
  }
  .company-name {
    position: absolute;
    left: 74px;
    top: 60px;
    margin: 0;
    font-family: "Saira", "Arial Black", sans-serif;
    font-weight: 700;
    font-size: 60px;
    line-height: 1.2;
    letter-spacing: 3px;
    color: var(--ink);
  }
  .slip-heading {
    position: absolute;
    left: 75px;
    top: 400px;
    margin: 0;
    font-weight: 400;
    font-size: 27.5px;
    line-height: 1.3;
    letter-spacing: -0.4px;
    color: var(--brand-blue);
  }
  .contact-list {
    position: absolute;
    left: 76px;
    top: 445px;
    margin: 0;
    padding: 0;
    list-style: none;
    display: flex;
    gap: 30px;
    font-size: 14px;
    color: var(--text-grey);
  }
  .contact-item {
    display: flex;
    align-items: center;
    gap: 6px;
  }
  .contact-icon {
    width: 15px;
    height: 15px;
  }
</style>
</head>
<body>
  <main class="compliment-slip">
    <div class="decor-area" role="img" aria-label="Decorative blue chevron and green diamond line pattern"></div>

    <h1 class="company-name">VORBIN</h1>

    <h2 class="slip-heading">WITH COMPLIMENTS</h2>

    <ul class="contact-list">
      <li class="contact-item">
        <svg class="contact-icon" viewBox="0 0 16 16" aria-hidden="true">
          <g fill="none" stroke="var(--brand-blue)" stroke-width="1.2">
            <circle cx="8" cy="8" r="6.5"/>
            <ellipse cx="8" cy="8" rx="3" ry="6.5"/>
            <line x1="1.5" y1="8" x2="14.5" y2="8"/>
            <line x1="2.5" y1="4.8" x2="13.5" y2="4.8"/>
            <line x1="2.5" y1="11.2" x2="13.5" y2="11.2"/>
          </g>
        </svg>
        <span>www.vorbin.example</span>
      </li>
      <li class="contact-item">
        <svg class="contact-icon" viewBox="0 0 16 16" aria-hidden="true">
          <rect x="2" y="4" width="12" height="8" fill="var(--brand-blue)"/>
          <polyline points="2,4 8,9 14,4" fill="none" stroke="#fff" stroke-width="1"/>
        </svg>
        <span>info@vorbin.example</span>
      </li>
    </ul>
  </main>
</body>
</html>
```